The Hidden Harvest Summit (Poster or Color Flyer)

Unique and not too traditional design with Wording:
The Hidden Harvest Summit: The Deeper Message of God's Relentless Love
Friday Aug. 5 - Sunday the 7th
Denver 2016
www.TheHarvestSummitEvent.com
Updates
Project Deadline Extended
Reason: Our first experience with this type of design service was with 42Sketchery, and we received 140 designs within a week.
We received only 2 designers submissions by our first 5 days with Artisan Pool. We received an email that our time would be extended, which is much appreciated. The last 24 hours has brought in several new designs - which is great. However, we have a team of reviewers on our end - and due to Christmas break, will not be able to make a decision until January 4 or 5.
Can our deadline be moved to January 5? (at no charge?)
THANKS,
Glen
Target Market(s)
General public. Professors. Pastors.
Requirements
Must have
- Basic info above.
Nice to have
- Subtle verses tucked into the graphics
- See www.TheKQRs.com for some of these,
- such as Romans 11:32, 1 John 2:2, 1 Timothy 4:10, John 12:32
Should not have
- Typical religious appearance.

```html
<!DOCTYPE html>
<html lang="en">
<head>
<meta charset="utf-8">
<title>The Hidden Harvest Summit</title>
<link href="https://fonts.googleapis.com/css2?family=Alegreya:wght@400;700;900&display=swap" rel="stylesheet">
<style>
  :root {
    --sky-white: #fffdf2;
    --sun-yellow: #f8ef4a;
    --warm-orange: #f2a640;
    --deep-red: #e3101a;
    --dark-red: #b9070f;
    --verse-ink: rgba(205, 205, 70, 0.5);
    --accent-lime: #e6ee6c;
    --title-white: #ffffff;
    --title-shadow: #2a0a08;
  }
  html, body {
    margin: 0;
    padding: 0;
    overflow: hidden;
    background: #ffffff;
  }
  .poster {
    position: relative;
    width: 848px;
    height: 1200px;
    overflow: hidden;
    font-family: "Alegreya", Georgia, serif;
    background:
      radial-gradient(ellipse 60% 35% at 50% 14%, var(--sky-white) 0%, rgba(255,253,240,0) 75%),
      linear-gradient(180deg, #fffbe0 0%, #fdf7a0 22%, var(--sun-yellow) 40%, #f6e24a 55%, #f2c34a 66%, var(--warm-orange) 76%);
  }
  .hero-figure {
    position: absolute;
    left: 60px;
    top: 40px;
    width: 728px;
    height: 760px;
    background:
      radial-gradient(ellipse 50% 55% at 50% 55%, rgba(242,168,72,0.55) 0%, rgba(242,168,72,0.25) 55%, rgba(242,168,72,0) 100%),
      radial-gradient(ellipse 45% 30% at 50% 95%, rgba(236,90,50,0.55) 0%, rgba(236,90,50,0) 100%);
  }
  .verses {
    position: absolute;
    left: 42px;
    top: 46px;
    width: 756px;
    color: var(--verse-ink);
  }
  .verse {
    position: relative;
    margin: 0 0 20px;
  }
  .verse:nth-child(3) { margin-bottom: 24px; }
  .verse-text {
    margin: 0;
    font-weight: 700;
    font-size: 35px;
    line-height: 45px;
    text-transform: uppercase;
  }
  .verse-line {
    display: block;
    text-align: justify;
    text-align-last: justify;
  }
  .verse-line.is-last {
    text-align: left;
    text-align-last: left;
  }
  .verse-ref {
    position: absolute;
    right: 14px;
    bottom: 4px;
    font-weight: 700;
    font-size: 16px;
    line-height: 20px;
    text-transform: uppercase;
  }
  .verse-ref.is-below {
    bottom: -32px;
  }
  .base-band {
    position: absolute;
    left: 0;
    top: 690px;
    width: 848px;
    height: 510px;
  }
  .title-block {
    position: absolute;
    left: 0;
    top: 794px;
    width: 848px;
    text-align: center;
  }
  .event-title {
    margin: 0;
    font-weight: 900;
    font-size: 64px;
    line-height: 80px;
    color: var(--title-white);
    text-transform: uppercase;
    text-shadow: 3px 4px 0 var(--title-shadow);
  }
  .rule {
    height: 0;
    border: 0;
    margin: 0 auto;
  }
  .rule-white {
    width: 815px;
    border-top: 2px solid var(--title-white);
    margin-top: 10px;
  }
  .event-subtitle {
    margin: 16px 0 18px;
    font-weight: 900;
    font-size: 33px;
    line-height: 40px;
    color: var(--title-white);
    text-transform: uppercase;
    text-shadow: 2px 2px 0 var(--title-shadow);
  }
  .rule-lime {
    width: 694px;
    border-top: 2px solid var(--accent-lime);
  }
  .event-dates {
    margin: 16px 0 0;
    font-weight: 400;
    font-size: 31px;
    line-height: 38px;
    color: var(--accent-lime);
    text-transform: uppercase;
  }
  .event-dates sup {
    text-transform: none;
    font-size: 17px;
  }
  .event-dates .sep { margin: 0 16px; }
  .event-url {
    margin: 8px 0 0;
    font-weight: 400;
    font-size: 24px;
    color: var(--accent-lime);
    text-transform: uppercase;
    letter-spacing: 1.5px;
  }
</style>
</head>
<body>
<main class="poster">
  <div class="hero-figure" role="img" aria-label="Glowing translucent human figure with arms open, looking upward, in orange and red tones"></div>

  <section class="verses">
    <div class="verse">
      <p class="verse-text">
        <span class="verse-line">For God has consigned all to</span>
        <span class="verse-line">disobedience so that he may have</span>
        <span class="verse-line is-last">mercy on them all.</span>
      </p>
      <span class="verse-ref">Romans 11:32</span>
    </div>
    <div class="verse">
      <p class="verse-text">
        <span class="verse-line">He is the atoning sacrifice for our</span>
        <span class="verse-line">sins, and not only for ours ut also for</span>
        <span class="verse-line is-last">the sins of the whole world.</span>
      </p>
      <span class="verse-ref">1 John 2:2</span>
    </div>
    <div class="verse">
      <p class="verse-text">
        <span class="verse-line">And we have seen and testify that the</span>
        <span class="verse-line">Father has sent his Son to be the</span>
        <span class="verse-line is-last">Savior of the world.</span>
      </p>
      <span class="verse-ref">John 12:32</span>
    </div>
    <div class="verse">
      <p class="verse-text">
        <span class="verse-line">That is why we labor because we trust</span>
        <span class="verse-line">in the living God who is the Savior of</span>
        <span class="verse-line is-last">all men, especially those who believe.</span>
      </p>
      <span class="verse-ref is-below">1 Timothy 4:10</span>
    </div>
  </section>

  <svg class="base-band" viewBox="0 0 848 510" aria-hidden="true">
    <defs>
      <linearGradient id="bandRed" x1="0" y1="0" x2="0" y2="1">
        <stop offset="0" stop-color="#e5141c"/>
        <stop offset="1" stop-color="#b9070f"/>
      </linearGradient>
    </defs>
    <path d="M0 70 Q424 -8 848 70" fill="none" stroke="#e6ee6c" stroke-width="10"/>
    <path d="M0 84 Q424 6 848 84 L848 510 L0 510 Z" fill="url(#bandRed)"/>
  </svg>

  <header class="title-block">
    <h1 class="event-title">The Hidden Harvest<br>Summit:</h1>
    <hr class="rule rule-white">
    <p class="event-subtitle">The Deeper Message of God's Relentless Love</p>
    <hr class="rule rule-lime">
    <p class="event-dates">Friday Aug. 5 - Sunday the 7<sup>th</sup><span class="sep">|</span>Denver 2016</p>
    <p class="event-url">www.TheHarvestSummitEvent.com</p>
  </header>
</main>
</body>
</html>
```